TARPLOAD business card design

TARPLOAD is a manufacturer of skip bags supplying both the domestic and commercial market. We wish to convey core characteristics of strength, professionalism and reliability to our customers. We are after a business card that uses our company colours of black and yellow as well as incorporating our logo. Our customers are predominantly in the construction or hardware industry. It is important the cards are professional as we are a small company wishing to appear larger than we actually are. more info on the company and product available at www.tarpload-example.com.au

Target Market(s)

hardware buyers, contruction company owners

Industry/Entity Type

Construction

Requirements
Must have
• company colours of black and yellow - No other colours or variation of yellow black. our company logo. card design must convey "tough"
• Card design must be landscape
• Details to be included on the card are:
• Name and Tiltle
• Phone number : 1300 41 62 53
• Mobile: 0452 718 903
• Fax: 03 9617 4852
• email: dale.hendry@tarpload-example.com.au
• address: PO Box 517, Kelvindale, VIC,3294
• Text in white when on a black background
Nice to have
• I like the idea of the back of the card being black with lighter circle area in the middle with black logo in the centre. Similar to the attached "iconic" card

```html
<!DOCTYPE html>
<html lang="en">
<head>
<meta charset="utf-8">
<title>TARPLOAD business card</title>
<link rel="stylesheet" href="https://fonts.googleapis.com/css2?family=Arimo:wght@400;700&display=swap">
<style>
  :root {
    --backdrop: #c4c5c7;
    --ink: #1f1a17;
    --paper: #ffffff;
    --brand-yellow: #e3c400;
    --muted-panel: #5f5a56;
  }
  html, body {
    margin: 0;
    padding: 0;
    overflow: hidden;
  }
  body {
    width: 978px;
    height: 1200px;
    background: var(--backdrop);
    position: relative;
    font-family: "Arimo", Arial, sans-serif;
    color: var(--ink);
  }
  .card {
    position: absolute;
    left: 117px;
    width: 743px;
    height: 454px;
    overflow: hidden;
  }
  .card--front { top: 106px; background: var(--paper); }
  .card--back { top: 640px; background: var(--ink); }

  .front-shape {
    position: absolute;
    inset: 0;
    width: 100%;
    height: 100%;
  }
  .brand-tile {
    position: absolute;
    display: flex;
    align-items: center;
    justify-content: center;
  }
  .card--front .brand-tile {
    left: 49px;
    top: 49px;
    width: 177px;
    height: 160px;
    background: var(--brand-yellow);
  }
  .card--back .brand-tile {
    left: 277px;
    top: 143px;
    width: 189px;
    height: 169px;
    background: var(--muted-panel);
  }
  .brand-name {
    font-weight: 700;
    font-size: 26px;
    letter-spacing: 0.5px;
    color: var(--ink);
  }
  .person {
    position: absolute;
    left: 49px;
    top: 322px;
  }
  .person__name {
    font-weight: 700;
    font-size: 28px;
    line-height: 28px;
    margin: 0;
  }
  .person__title {
    font-size: 16px;
    line-height: 18px;
    margin: 0;
  }
  .contact {
    position: absolute;
    left: 342px;
    top: 290px;
    margin: 0;
    padding: 0;
    list-style: none;
    font-size: 16.5px;
    line-height: 23.8px;
    white-space: nowrap;
  }
</style>
</head>
<body>
  <section class="card card--front" aria-label="Card front">
    <svg class="front-shape" viewBox="0 0 743 454" aria-hidden="true">
      <polygon points="0,0 743,0 743,128 339.5,254 0,254" fill="var(--ink)"/>
      <rect x="0" y="438" width="743" height="16" fill="var(--ink)"/>
    </svg>
    <div class="brand-tile">
      <span class="brand-name">TARPLOAD</span>
    </div>
    <div class="person">
      <p class="person__name">Name</p>
      <p class="person__title">General manager</p>
    </div>
    <ul class="contact">
      <li>Phone number : 1300 41 62 53</li>
      <li>Mobile: 0452 718 903</li>
      <li>Fax: 03 9617 4852</li>
      <li>email: dale.hendry@tarpload-example.com.au</li>
      <li>address: PO Box 517, Kelvindale, VIC,3294</li>
    </ul>
  </section>

  <section class="card card--back" aria-label="Card back">
    <div class="brand-tile">
      <span class="brand-name">TARPLOAD</span>
    </div>
  </section>
</body>
</html>
```